New Web Design Project

Number of Pages Required

1 page

Requirements
Must have
• An Overview / Background of the Business & Services(not for profit rescue animal farm)
• The Target Market / Audience you are trying to reach (animal lovers)
• Design Specifics; any preferences or ideas for Style, Colour, Imagery, etc (no preferences)

```html
<!DOCTYPE html>
<html lang="en">
<head>
<meta charset="utf-8">
<title>Meadow Rest Farm Sanctuary</title>
<link rel="stylesheet" href="https://fonts.googleapis.com/css2?family=Gelasio:ital,wght@0,400;0,500;1,400&family=Arimo:ital,wght@0,400;1,400&display=swap">
<style>
:root{
  --olive:#2e3300;
  --page:#f9f9f9;
  --band:#f3f3f3;
  --ink:#2b2b2b;
  --muted:#9a9a9a;
  --peach:#fcdcc7;
  --cream:#f3ecd9;
  --white:#ffffff;
}
*{margin:0;padding:0;box-sizing:border-box}
html,body{width:1200px;height:2335px;overflow:hidden}
body{background:var(--page);font-family:"Arimo",Arial,sans-serif;color:var(--ink);position:relative}
h1,h2,h3{font-weight:400}
.serif{font-family:"Gelasio",Georgia,serif;font-weight:400}
.abs{position:absolute}

.site-header{position:absolute;left:0;top:0;width:1200px;height:67px;background:var(--olive)}
.main-nav{position:absolute;top:20px;left:640px}
.main-nav a{color:var(--white);text-decoration:none;font-size:10.5px;position:absolute;white-space:nowrap}
.main-nav a.active::after{content:"";position:absolute;left:0;right:0;bottom:-5px;height:1.5px;background:var(--white)}

.hero-photo{left:0;top:67px;width:1200px;height:584px;background:linear-gradient(180deg,#4f8a1c 0%,#6aa62c 30%,#6c8f2f 60%,#556b26 100%)}
.hero-title{left:423px;top:122px;font-size:30px;line-height:36px;color:var(--white);letter-spacing:.6px;white-space:nowrap}
.hero-lead{left:423px;top:212px;width:310px;font-size:9.5px;line-height:15px;color:var(--white)}
.btn-friend{left:420px;top:257px;width:129px;height:31px;border-radius:16px;background:var(--peach);color:var(--ink);font-size:11px;display:flex;align-items:center;justify-content:center;text-decoration:none;letter-spacing:.3px}

.about-photo{left:341px;top:697px;width:185px;height:246px;background:linear-gradient(180deg,#6f9ac9 0%,#3f6b2c 45%,#5b8f2c 100%)}
.about-title{left:601px;top:703px;font-size:22px;letter-spacing:1px;white-space:nowrap}
.about-text{left:602px;top:778px;width:274px;font-size:9px;line-height:14.5px;text-align:justify;color:#333}

.section-title{left:0;width:1200px;text-align:center;font-size:21px;line-height:28px;letter-spacing:.8px;color:#333}

.gallery-item{width:258px;height:184px}
.tone-horse{background:linear-gradient(135deg,#c9a56a 0%,#8c6a3a 55%,#e6d6b0 100%)}
.tone-cow{background:linear-gradient(180deg,#2f4f9a 0%,#6a86c4 40%,#e9d3b3 70%,#a48b5f 100%)}

.involved-band{left:0;top:1836px;width:1200px;height:273px;background:var(--band)}
.involved-title{left:185px;top:1801px;font-size:21.5px;line-height:28.5px;letter-spacing:.6px;color:#333;white-space:nowrap}
.involved-text{left:185px;top:1903px;width:250px;font-size:7.5px;line-height:11.5px;font-style:italic;color:var(--muted)}
.involved-photo{left:593px;top:1765px;width:420px;height:281px;background:linear-gradient(180deg,#c7d7e4 0%,#7e8f5c 35%,#5d7a3a 70%,#8a6b4a 100%)}

.site-footer{left:0;top:2109px;width:1200px;height:226px;background:var(--olive);color:var(--cream)}
.footer-heading{font-size:21px;line-height:28px;letter-spacing:.8px;color:var(--white);white-space:nowrap}
.contact-line{display:flex;align-items:center;gap:12px;font-size:11.5px;line-height:15px;color:var(--cream);letter-spacing:.4px;white-space:nowrap}
.contact-line svg{flex:none}
</style>
</head>
<body>

<header class="site-header">
  <nav class="main-nav">
    <a href="#about" style="left:0">About the sanctuary</a>
    <a href="#animals" class="active" style="left:117px">Our Animals</a>
    <a href="#involved" style="left:199px">Get Involved</a>
    <a href="#contacts" style="left:283px">Contacts</a>
  </nav>
</header>

<div class="abs hero-photo" role="img" aria-label="Lamb leaning on a resting sheep in a green meadow"></div>
<h1 class="abs hero-title serif">Not only people<br>need care, we do too...</h1>
<p class="abs hero-lead">Welcome to our Farm. We live according to our the values and encourage others to do the same.</p>
<a class="abs btn-friend serif" href="#involved">Make a friend</a>

<section id="about">
  <div class="abs about-photo" role="img" aria-label="Wooden fence in a sunny wooded pasture"></div>
  <h2 class="abs about-title serif">About SANCTUARY</h2>
  <p class="abs about-text">We operates local large farm animal rescue. Eventually we rescue farm animals and educates the public about the choice for a compassionate lifestyle. Every year, we assist with urgent placement needs providing a safe and loving forever home to our own feathered and furry family. When our shelters are full, we depend on compassionate people who want to make a direct difference for a suffering sheep, pony or other farm animal and place our rescued animal friends into their loving homes.</p>
</section>

<section id="animals">
  <h2 class="abs section-title serif" style="top:1038px">Here a Gallery About Our<br>Sanctuary and Fury Friends</h2>
  <div class="abs gallery-item tone-horse" style="left:173px;top:1150px" role="img" aria-label="Pony grazing in dry grass"></div>
  <div class="abs gallery-item tone-cow" style="left:472px;top:1150px" role="img" aria-label="Cows standing under a blue sky"></div>
  <div class="abs gallery-item tone-horse" style="left:764px;top:1150px" role="img" aria-label="Pony grazing in dry grass"></div>
  <div class="abs gallery-item tone-cow" style="left:173px;top:1373px" role="img" aria-label="Cows standing under a blue sky"></div>
  <div class="abs gallery-item tone-horse" style="left:472px;top:1373px" role="img" aria-label="Pony grazing in dry grass"></div>
  <div class="abs gallery-item tone-cow" style="left:764px;top:1373px" role="img" aria-label="Cows standing under a blue sky"></div>
</section>

<section id="involved">
  <div class="abs involved-band"></div>
  <h2 class="abs section-title serif" style="top:1665px">Here a Gallery About Our<br>Sanctuary and Fury Friends</h2>
  <h2 class="abs involved-title serif">You Too Are Welcome<br>To Get Involved And Enjoy Doing<br>Your Part.</h2>
  <p class="abs involved-text">We create events and provide awareness both here at the sanctuary and out in the community. We do educate animal lovers and help encourage others to get involved and share what they learn with their families and friends. We want people to experience compassion, have fun and do cool things together.</p>
  <div class="abs involved-photo" role="img" aria-label="Woman with braided hair greeting ponies on a hillside"></div>
</section>

<footer class="abs site-footer" id="contacts">
  <h3 class="abs footer-heading serif" style="left:235px;top:43px">For questions<br>and suggestions</h3>
  <div class="abs contact-line serif" style="left:235px;top:124px">
    <svg width="24" height="16" viewBox="0 0 24 16" fill="none" stroke="#f3ecd9" stroke-width="1.2"><rect x="1" y="1" width="22" height="14"/><path d="M1 1l11 8 11-8M1 15l8-7M23 15l-8-7"/></svg>
    <span>hello@meadowrest.org</span>
  </div>
  <div class="abs contact-line serif" style="left:235px;top:162px">
    <svg width="24" height="18" viewBox="0 0 24 18" fill="none" stroke="#f3ecd9" stroke-width="1.2"><path d="M2 6c0-3 4-4 10-4s10 1 10 4v2h-5V6H7v2H2z"/><rect x="5" y="9" width="14" height="8"/><circle cx="12" cy="13" r="2"/></svg>
    <span>+1 555 010 22 44</span>
  </div>

  <h3 class="abs footer-heading serif" style="left:517px;top:43px">We are waiting<br>for your visit</h3>
  <div class="abs contact-line serif" style="left:517px;top:121px">
    <svg width="16" height="24" viewBox="0 0 16 24" fill="none" stroke="#f3ecd9" stroke-width="1.2"><path d="M8 23S1 13 1 8a7 7 0 0 1 14 0c0 5-7 15-7 15z"/><circle cx="8" cy="8" r="2.5"/></svg>
    <span>Millbrook, Local Farm 1st<br>(Entrance from road)</span>
  </div>
  <div class="abs contact-line serif" style="left:517px;top:160px">
    <svg width="16" height="24" viewBox="0 0 16 24" fill="none" stroke="#f3ecd9" stroke-width="1.2"><path d="M8 23S1 13 1 8a7 7 0 0 1 14 0c0 5-7 15-7 15z"/><circle cx="8" cy="8" r="2.5"/></svg>
    <span>Riverton, Hill Road 18</span>
  </div>
</footer>

</body>
</html>
```